Todo-list with focus on focus

We are writing todo app which is a to-do list/ outliner with focus support based on pomodoro method.

Attached are very rough mockups, but they are conceptually correct.

Main idea behind an app - minimum (unneeded) functionality and maximum benefit to the user.

So, everything must be very intuitive, fast, and without distractions (let's say Quince-style)

Target Market(s)

People who want to spend less time organizing their todo list than using it

Industry/Entity Type

It Support

Requirements
Must have
• Everything which is in mockups, maybe you can drop 1 or 2 if absolutely needed.
Nice to have
• 1. We would like to see such pallete here: http://www.huebinder.net/swatch/482716/Quiet_Harbor_Dusk but it's not mandatory.
If you propose some other pallete, please make sure it's beautiful.

2. It would be good to somehow indicate that project is a goal in project list, and task is a goal in goal's list

3. Inbox should be accessible easliy, probably by sticking it to the top of Projects list somehow.

4. If you are able to propose another way to deal with such amount of options to deal with tasks other than radial menu - you are free to do it, if it'll work.

5. Priority, tags - very nice to have if they will fit into conception.

6. Maybe you can add other stuff we have overlooked.
But, if added, it must be very simple and needed.

```html
<!DOCTYPE html>
<html lang="en">
<head>
<meta charset="utf-8">
<title>Focus To-do</title>
<link rel="stylesheet" href="https://fonts.googleapis.com/css2?family=Arimo:wght@400;700&display=swap">
<style>
:root{
  --bg:#ecebf0;
  --black:#0c0c0c;
  --panel:#2b2b2b;
  --panel-dark:#222222;
  --header:#2f2f2f;
  --line:#1a1a1a;
  --muted:#b9b9b9;
  --white:#f4f4f4;
  --orange:#f5a623;
  --orange-deep:#e0731a;
  --red:#c8101a;
  --cream:#f7f1de;
  --cream-line:#ddd6c2;
  --check:#f6e3b0;
  --brown:#5a3e2e;
  --paper-text:#8a8478;
}
*{box-sizing:border-box;margin:0;padding:0}
html,body{width:756px;height:1200px;overflow:hidden;background:var(--bg);font-family:"Arimo",Helvetica,Arial,sans-serif}
.stage{position:absolute;left:56px;top:30px;width:322px;height:570px;transform:scale(2);transform-origin:0 0;background:var(--panel);overflow:hidden}
.status-bar{position:absolute;left:0;top:0;width:322px;height:20px;background:var(--black);color:var(--white);font-size:12px;font-weight:700}
.status-bar .carrier{position:absolute;left:5px;top:3px;display:flex;align-items:center;gap:4px}
.status-bar .clock{position:absolute;left:0;right:0;top:3px;text-align:center}
.status-bar .right{position:absolute;right:6px;top:4px;display:flex;gap:6px;align-items:center}
.focus-panel{position:absolute;left:0;top:20px;width:256px;height:550px;background:var(--panel)}
.label{position:absolute;left:10px;color:var(--muted);font-size:13px}
.task-title{position:absolute;left:24px;top:28px;color:var(--orange);font-size:33px;font-weight:700}
.timer{position:absolute;left:22px;top:104px;color:var(--orange);font-size:46px;font-weight:700;letter-spacing:-1px}
.stop{position:absolute;left:166px;top:114px;width:76px;height:34px;border-radius:4px;background:linear-gradient(#e0141e,var(--red));color:#fff;font-size:14px;font-weight:700;display:flex;align-items:center;justify-content:center;border:1px solid #7a0008}
.counter{position:absolute;left:166px;top:172px;width:76px;height:34px;border-radius:4px;background:linear-gradient(#4a4a4a,#333);border:1px solid #171717;display:flex}
.counter span{flex:1;display:flex;align-items:center;justify-content:center;color:#fff;font-size:24px;font-weight:700}
.counter span+span{border-left:1px solid #1c1c1c}
.dots{position:absolute;left:80px;display:flex;gap:4px}
.dot{width:10px;height:10px;border-radius:50%;border:1.5px solid var(--orange)}
.dot.filled{background:var(--orange)}
.goal-list{position:absolute;left:0;top:217px;width:256px}
.spacer{height:22px;background:var(--panel-dark);border-top:1px solid var(--line)}
.section-head{height:23px;background:var(--header);color:var(--muted);font-size:13px;padding:4px 0 0 10px;border-top:1px solid #3a3a3a}
.goal{height:46px;display:flex;align-items:center;padding-left:24px;color:var(--white);font-size:16px;border-top:1px solid #363636;background:var(--panel)}
.box{width:21px;height:21px;border-radius:4px;background:var(--check);margin-right:13px;display:flex;align-items:center;justify-content:center}
.box.checked{background:var(--orange-deep)}
.outline-panel{position:absolute;left:256px;top:20px;width:66px;height:550px;background:var(--cream);box-shadow:-3px 0 6px rgba(0,0,0,.6)}
.outline-head{height:44px;background:linear-gradient(#f7a562,#ea8a3e)}
.outline-row{height:46px;border-bottom:1px solid var(--cream-line);color:var(--paper-text);font-size:16px;padding:14px 0 0 9px;white-space:nowrap;overflow:hidden}
.outline-row.sub{padding-left:29px}
.outline-row.sub2{padding-left:46px}
.outline-row.editing{padding:4px 0 0 7px}
.outline-row.editing span{display:block;height:36px;border:1px solid var(--orange);border-right:none;border-radius:5px 0 0 5px;background:#fff;color:#444;padding:8px 0 0 10px}
.compose{position:absolute;left:0;bottom:0;width:66px;height:60px;background:var(--brown);padding:10px 0 0 9px}
.compose span{display:block;height:38px;background:#fff;border-radius:5px 0 0 5px;color:#555;font-size:20px;padding:7px 0 0 9px}
</style>
</head>
<body>
<main class="stage">
  <header class="status-bar">
    <div class="carrier">
      <svg width="16" height="10" viewBox="0 0 16 10" aria-hidden="true"><g fill="#f4f4f4"><rect x="0" y="8" width="2" height="2"/><rect x="3" y="6" width="2" height="4"/><rect x="6" y="4" width="2" height="6"/><rect x="9" y="2" width="2" height="8"/><rect x="12" y="0" width="2" height="10"/></g></svg>
      <span>MERIDIAN</span><span>3G</span>
    </div>
    <div class="clock">4:20 AM</div>
    <div class="right">
      <svg width="9" height="9" viewBox="0 0 9 9" aria-hidden="true"><circle cx="4.5" cy="4.5" r="4" fill="#f4f4f4"/><path d="M4.5 2v2.7h2" stroke="#0c0c0c" stroke-width="1.2" fill="none"/></svg>
      <svg width="22" height="10" viewBox="0 0 22 10" aria-hidden="true"><rect x=".5" y=".5" width="19" height="9" rx="1.5" fill="none" stroke="#f4f4f4"/><rect x="2" y="2" width="16" height="6" fill="#f4f4f4"/><rect x="20" y="3" width="2" height="4" fill="#f4f4f4"/></svg>
    </div>
  </header>

  <section class="focus-panel">
    <p class="label" style="top:8px">I am focused on...</p>
    <h1 class="task-title">Task 1</h1>
    <p class="label" style="top:83px">Time left</p>
    <div class="timer">21:34</div>
    <div class="stop">Stop</div>
    <p class="label" style="top:171px;left:9px">Completed</p>
    <div class="dots" style="top:173px"><i class="dot filled"></i></div>
    <p class="label" style="top:192px;left:9px">Left</p>
    <div class="dots" style="top:194px"><i class="dot"></i><i class="dot"></i></div>
    <div class="counter"><span>−</span><span>+</span></div>

    <div class="goal-list">
      <div class="spacer"></div>
      <div class="section-head">Daily goals</div>
      <div class="goal"><span class="box checked"><svg width="14" height="12" viewBox="0 0 14 12" aria-hidden="true"><path d="M2 6l3.5 3.5L12 2" stroke="#fff" stroke-width="2.6" fill="none"/></svg></span>Daily goal 1</div>
      <div class="goal"><span class="box"></span>Daily goal 2</div>
      <div class="spacer"></div>
      <div class="section-head">Weekly goals</div>
      <div class="goal"><span class="box"></span>Weekly goal 1</div>
      <div class="spacer"></div>
      <div class="section-head">Life goals</div>
      <div class="goal"><span class="box"></span>Life goal 1</div>
    </div>
  </section>

  <aside class="outline-panel">
    <div class="outline-head"></div>
    <div class="outline-row">Task 1</div>
    <div class="outline-row sub">Subtask</div>
    <div class="outline-row sub">Subtask</div>
    <div class="outline-row sub2">Subtask</div>
    <div class="outline-row">Task 2</div>
    <div class="outline-row">Task 3</div>
    <div class="outline-row editing"><span>Task 4</span></div>
    <div class="compose"><span>Type</span></div>
  </aside>
</main>
</body>
</html>
```